Chatterly business page for Larkmere Rooms, London, UK

I need a Chatterly page for my business which lets rooms to psychologists and psychotherapists in Central London, UK. I have eleven rooms in total – 8 at Corvel Hall, London and 3 in Quillan St, London. Lots more info and text and pics at my website www.larkmererooms-demo.net. Might say 'Central London talking therapy rooms for rent at reasonable prices. Two Central London locations at Holborn and Bloomsbury. Located in listed buildings, giving a sense of place and containment, ideal for psychological therapies. Our renters are psychiatrists, psychologists and coaches who know how to work sympathetically together. Prestigious addresses. Excellent transport links with short walks to Brenwick Vale or Fenmarsh Abbey Road underground stations. Plenty of choice of excellent cafes, delicatessens etc for relaxation between clients. Elegant settings at a lower price. We offer significantly lower charges than equivalent providers by eliminating unnecessary expenses such as receptionists, large waiting rooms and fresh flowers. All rooms have high speed Wi-Fi for remote working. Flexibility. The rooms are available for half or whole day rental on a rolling contract basis, so you see the same colleagues each time. Having taken a day or half day, renters are welcome to arrange additional ad-hoc bookings either between themselves or with us for extra flexibility. Corvel Hall is a famous London landmark building dating from 1585 which survived the Tidewater Blaze of Eastmoor in 1666 and a Skarnkorps flying bomb in 1944. Quillan St is a charming pedestrianised street in the heart of Bloomsbury immediately adjacent to the Verdon Collection with lots of artisan shops, art galleries and cafes.

Psychologists, psychotherapists, psychiatrists, counsellors, life coaches etc.

Serif
Sans Serif

• Pics showing rooms. Reference to website larkmererooms-demo.net

```html
<!DOCTYPE html>
<html lang="en">
<head>
<meta charset="utf-8">
<title>Larkmere Rooms – Chatterly post concepts</title>
<link rel="stylesheet" href="https://fonts.googleapis.com/css2?family=Source+Serif+4:opsz,wght@8..60,400;8..60,500&display=swap">
<style>
  :root {
    --gold: #dfa50f;
    --card: #f2f2f2;
    --ink: #1c1c1c;
    --slate: #4c5a8c;
    --white: #ffffff;
    --serif: "Source Serif 4", Georgia, serif;
  }
  * { box-sizing: border-box; margin: 0; padding: 0; }
  html, body { width: 1200px; height: 812px; overflow: hidden; background: var(--white); }
  body { position: relative; font-family: var(--serif); color: var(--ink); }

  .banner {
    position: absolute; left: 0; top: 0; width: 1200px; height: 111px;
    background: var(--gold); color: var(--white);
    display: flex; align-items: center; justify-content: center;
    font-size: 37px; letter-spacing: -1.2px; font-weight: 400;
  }

  .post {
    position: absolute; top: 137px; width: 366px; height: 366px;
    background: var(--card); box-shadow: 0 1px 6px rgba(0,0,0,.18);
  }
  .post--sizes { left: 36px; }
  .post--central { left: 417px; background: var(--gold); }
  .post--relax { left: 798px; }

  .abs { position: absolute; white-space: nowrap; line-height: 1; }

  .photo { position: absolute; }
  .photo--sizes {
    left: 20px; top: 99px; width: 327px; height: 208px;
    border: 5px solid var(--gold); border-radius: 18px;
    background: linear-gradient(100deg, #3a2f2a 0%, #8c7a68 30%, #e6d8c6 55%, #c9b49a 80%, #6d5646 100%);
  }
  .photo--central {
    left: 19px; top: 91px; width: 329px; height: 214px;
    border: 5px solid var(--white);
    background: linear-gradient(90deg, #e3d3bc 0%, #9c917f 25%, #555047 55%, #7e7868 80%, #a3a89a 100%);
  }
  .photo--relax {
    left: 21px; top: 87px; width: 323px; height: 193px; border-radius: 12px;
    background: linear-gradient(110deg, #6e6862 0%, #b5aea6 35%, #ece7e1 60%, #8d8c8e 85%, #3e5a8e 100%);
  }

  .title-lg { font-size: 33px; letter-spacing: -1.3px; }
  .title-md { font-size: 25px; letter-spacing: -1px; }
  .accent { color: var(--gold); }

  .size-list { left: 250px; top: 22px; width: 90px; height: 60px; }
  .size-list span { position: absolute; right: 14px; font-size: 13px; letter-spacing: -.4px; }

  .brand { font-size: 20px; letter-spacing: -.7px; }
  .btn {
    position: absolute; border-radius: 14px; font-size: 15px;
    display: flex; align-items: center; justify-content: center; letter-spacing: -.3px;
  }
  .btn--gold { background: var(--gold); color: var(--white); }
  .btn--white { background: var(--white); color: var(--ink); }

  .spaced { font-size: 19px; letter-spacing: 4.4px; color: var(--white); }

  .mark { display: flex; align-items: center; gap: 4px; font-size: 10px; color: var(--gold); }
  .mark i { display: block; width: 12px; height: 12px; background: var(--gold); }

  .message {
    position: absolute; left: 0; top: 550px; width: 1200px; text-align: center;
    font-size: 32px; line-height: 39px; letter-spacing: -1.3px; color: #111;
    text-shadow: 0 3px 6px rgba(0,0,0,.18);
  }
  .message .thanks { margin-top: 38px; }
</style>
</head>
<body>
  <header class="banner">Chatterly business page for Larkmere Rooms, London, UK</header>

  <section class="post post--sizes">
    <div class="abs title-lg" style="left:21px;top:26px;">Relaxing rooms</div>
    <div class="abs title-md" style="left:21px;top:58px;">in <span class="accent">three</span> different sizes</div>
    <div class="abs size-list">
      <span style="top:0">Small</span>
      <span style="top:22px">Medium</span>
      <span style="top:45px">Large</span>
      <svg width="10" height="60" style="position:absolute;right:0;top:0" aria-hidden="true">
        <line x1="5" y1="6" x2="5" y2="51" stroke="var(--gold)" stroke-width="2"/>
        <circle cx="5" cy="6" r="3" fill="var(--gold)"/>
        <circle cx="5" cy="28" r="3" fill="var(--gold)"/>
        <circle cx="5" cy="51" r="3" fill="var(--gold)"/>
      </svg>
    </div>
    <div class="photo photo--sizes" role="img" aria-label="Therapy room corner with armchair, striped cushion, side table and lamp by leaded windows"></div>
    <div class="abs brand" style="left:21px;top:324px;">Larkmere Rooms</div>
    <div class="btn btn--gold" style="left:261px;top:323px;width:84px;height:27px;">Book Now</div>
  </section>

  <section class="post post--central">
    <div class="abs title-lg" style="left:19px;top:30px;color:var(--white);font-size:29px;">Central London</div>
    <div class="abs spaced" style="left:19px;top:61px;">talking therapy rooms</div>
    <div class="photo photo--central" role="img" aria-label="Therapy room with grey armchair, lamp and radiator beneath tall leaded windows"></div>
    <div class="abs brand" style="left:19px;top:319px;color:var(--white);">Larkmere Rooms</div>
    <div class="btn btn--white" style="left:266px;top:317px;width:82px;height:24px;">Book Now</div>
  </section>

  <section class="post post--relax">
    <div class="abs" style="left:21px;top:21px;font-size:22px;letter-spacing:-.9px;">All you need is</div>
    <div class="abs" style="left:21px;top:41px;font-size:35px;letter-spacing:-1.5px;color:var(--slate);">Relaxing!</div>
    <div class="abs mark" style="right:22px;top:24px;"><i></i>Larkmere Rooms</div>
    <div class="photo photo--relax" role="img" aria-label="Bright therapy room with grey sofa, armchair, side table and blue patterned rug"></div>
    <div class="abs" style="left:21px;top:296px;font-size:27px;letter-spacing:-1.2px;">Elegant settings at</div>
    <div class="abs" style="left:21px;top:322px;font-size:22px;letter-spacing:-.8px;color:var(--slate);">a lower price</div>
    <div class="btn btn--gold" style="left:261px;top:316px;width:84px;height:27px;">Book Now</div>
  </section>

  <div class="message">
    <p>I have designed 3 sample posts to promote your chatterly service page.</p>
    <p>Furthermore, if you provide me more images and details I can design more creative</p>
    <p>according to several areas such as memes, ads, propmotions, features, facts etc.</p>
    <p>Hope you like my proposal and I request you to rate my concept too.</p>
    <p class="thanks">Thank you!</p>
  </div>
</body>
</html>
```